Boutique Store Selling Antiques and Unique Finds

I need a Web Page designed for my Store Called "Harrow Lane". I would like a very classic, muted design that looks European when pulled up. I will be selling Antiques from all over the world and Unique finds that have reproduced. I will also be selling high-end purses and jewelry with unique, reasonable products for the every-day buyer as well.

Target Market(s)

25-70 year old men and women;)

Coding

Number of Pages Required

1 page

Colors

Designer to choose only greyscale colors for use in the design.

Requirements
Must have
• I want it

```html
<!DOCTYPE html>
<html lang="en">
<head>
<meta charset="utf-8">
<title>Harrow Lane — Antiques &amp; Unique Finds</title>
<link href="https://fonts.googleapis.com/css2?family=Jost:wght@400;500;600&family=Cinzel:wght@400;500&display=swap" rel="stylesheet">
<style>
:root{
  --ink:#111;
  --text:#333;
  --muted:#666;
  --line:#bdbdbd;
  --paper:#fff;
  --tint:#f1f0ee;
  --panel:#eae8e4;
  --accent:#23332f;
  --footer:#000;
  --footer-text:#e6e6e6;
}
*{margin:0;padding:0;box-sizing:border-box}
html,body{width:1200px;height:3626px;overflow:hidden;background:var(--paper)}
body{position:relative;font-family:'Jost',sans-serif;color:var(--text)}
.abs{position:absolute}
.serif{font-family:'Cinzel',serif}

/* header */
.header{position:absolute;left:0;top:0;width:1200px;height:114px;border-bottom:1px solid #ddd}
.header a{color:var(--text);text-decoration:none;font-size:13px;letter-spacing:.3px}
.header .nav{position:absolute;top:72px}
.home-line{position:absolute;left:92px;top:110px;width:53px;height:3px;background:var(--ink)}
.brand{position:absolute;left:0;width:1210px;text-align:center;top:58px;font-family:'Cinzel',serif;font-size:26px;letter-spacing:4px;color:var(--ink)}
.brand-dot{display:inline-block;width:9px;height:9px;border-radius:50%;background:var(--ink);margin-right:10px;vertical-align:middle}

/* hero */
.hero{position:absolute;left:0;top:114px;width:1200px;height:608px;background:radial-gradient(circle at 70% 40%,#8b6a3a,#5a3e1e 55%,#2c1d0e)}
.hero-card{position:absolute;left:103px;top:158px;width:415px;height:271px;background:rgba(255,255,255,.55);border:2px solid rgba(255,255,255,.85)}
.hero-card .inner{position:absolute;inset:6px;border:1px solid rgba(255,255,255,.7)}
.hero-kicker{position:absolute;top:77px;width:100%;text-align:center;font-family:'Cinzel',serif;font-size:17px;letter-spacing:3px;color:#222}
.hero-title{position:absolute;top:100px;width:100%;text-align:center;font-family:'Cinzel',serif;font-size:28px;line-height:36px;color:#111}
.hero-btn{position:absolute;left:124px;top:186px;width:167px;height:35px;border:2px solid #111;font-family:'Jost';font-weight:600;font-size:12px;letter-spacing:2px;text-align:center;line-height:31px;color:#111}
.dot{position:absolute;width:16px;height:16px;border-radius:50%;background:#fff;top:582px}
.dot.ring{width:30px;height:30px;background:none;border:2px solid #fff;top:575px}

/* section titles */
.sec-title{position:absolute;left:0;width:1200px;text-align:center;font-size:28px;letter-spacing:4px;color:var(--ink);font-weight:400}
.sec-title b{font-weight:600}
.sec-rule{position:absolute;left:585px;width:32px;height:3px;background:var(--accent)}

/* product categories */
.cat{position:absolute;top:848px;width:274px;height:259px;border:1px solid #999;background:#fff}
.cat .img{position:absolute;inset:7px;background:linear-gradient(#8a7a66,#3e352c)}
.cat .label{position:absolute;left:14px;right:14px;bottom:12px;height:46px;background:#f3f1ec;border:1px solid #ddd;font-family:'Cinzel',serif;font-size:17px;letter-spacing:2px;text-align:center;line-height:46px;color:#111}

/* about */
.about{position:absolute;left:0;top:1162px;width:1200px;height:557px;background:linear-gradient(90deg,#2c221c,#5a3b2c 35%,#3a2a20 60%,#6b4a35)}
.about-card{position:absolute;left:655px;top:122px;width:447px;height:317px;background:#ebe8e3}
.about-card .inner{position:absolute;inset:10px;border:1px solid #555}
.about-kicker{position:absolute;top:80px;width:100%;text-align:center;font-size:14px;letter-spacing:2px;color:#222}
.about-title{position:absolute;top:100px;width:100%;text-align:center;font-size:29px;letter-spacing:4px;color:#111}
.about-title b{font-weight:600}
.about-text{position:absolute;top:156px;left:40px;right:40px;text-align:center;font-size:11.5px;line-height:21px;color:#333}
.btn{position:absolute;background:var(--accent);color:#fff;font-weight:500;text-align:center;letter-spacing:.5px}

/* shop online */
.card{position:absolute;top:1853px;width:326px;height:298px;border:1px solid #999;background:#fff}
.card .img{position:absolute;left:0;top:0;width:100%;height:221px}
.card .name{position:absolute;top:240px;width:100%;text-align:center;font-size:15px;letter-spacing:1px;color:#222}
.card .price{position:absolute;top:263px;width:100%;text-align:center;font-size:14px;font-weight:600;color:#111}
.sdot{position:absolute;top:2206px;width:7px;height:7px;border-radius:50%;background:#ccc}

/* popular */
.popular{position:absolute;left:0;top:2270px;width:1200px;height:638px;background:var(--tint)}
.pop{position:absolute;top:142px;width:496px;height:411px;background:#fff;border:1px solid #999}
.pop .img{position:absolute;left:0;top:0;width:100%;height:310px}
.pop .name{position:absolute;top:334px;width:100%;text-align:center;font-size:17px;letter-spacing:1px;color:#222}
.pop .price{position:absolute;top:361px;width:100%;text-align:center;font-size:14px;font-weight:600;color:#111}

/* newsletter */
.nl-title{position:absolute;left:0;width:1200px;text-align:center;font-size:27px;letter-spacing:4px;color:var(--ink)}
.field{position:absolute;top:3098px;height:46px;border:1px solid #888;background:#fff;font-size:12px;padding-left:18px;line-height:44px;color:#333}

/* footer */
.footer{position:absolute;left:0;top:3263px;width:1200px;height:363px;background:var(--footer);color:var(--footer-text)}
.fcol{position:absolute;top:78px}
.fcol h4{font-weight:400;font-size:13px;margin-bottom:10px;color:#fff}
.fcol li{list-style:none;font-size:10px;line-height:25px;color:#ccc}
.fdiv{position:absolute;top:67px;width:1px;height:141px;background:#333}
.fbar{position:absolute;left:0;top:278px;width:1200px;height:1px;background:#222}
.fsmall{position:absolute;top:316px;font-size:10px;color:#aaa}
.fbrand{position:absolute;left:0;width:1200px;text-align:center;top:320px;font-family:'Cinzel',serif;font-size:20px;letter-spacing:3px;color:#fff}
</style>
</head>
<body>

<header class="header">
  <a class="abs" style="left:99px;top:19px;font-size:11px">MY ACCOUNT</a>
  <a class="abs" style="left:1033px;top:23px;font-size:11px">BASKET (0)</a>
  <a class="nav" style="left:96px;color:#111">HOME</a>
  <a class="nav" style="left:184px">SHOP ONLINE</a>
  <a class="nav" style="left:322px">PRODUCTS</a>
  <a class="nav" style="left:801px">DISCOVER</a>
  <a class="nav" style="left:915px">BLOGS</a>
  <a class="nav" style="left:1005px">CONTACT US</a>
  <div class="home-line"></div>
  <div class="brand"><span class="brand-dot"></span>HARROW LANE</div>
</header>

<section class="hero" role="img" aria-label="Photograph of antique brass telescope, compass and globe on an old map">
  <div class="hero-card">
    <div class="inner"></div>
    <div class="hero-kicker">SHOP NOW</div>
    <div class="hero-title">ANTIQUES FROM<br>ALL OVER THE WORLD</div>
    <div class="hero-btn">VIEW PRODUCTS</div>
  </div>
  <div class="dot" style="left:538px"></div>
  <div class="dot ring" style="left:566px"></div>
  <div class="dot" style="left:608px"></div>
</section>

<h2 class="sec-title" style="top:766px">OUR <b>PRODUCTS</b></h2>
<div class="sec-rule" style="top:806px"></div>

<div class="cat" style="left:46px"><div class="img" role="img" aria-label="Antique iron helmet on a stack of books"></div><div class="label">ANTIQUES</div></div>
<div class="cat" style="left:328px"><div class="img" role="img" aria-label="Jewelled antique crown" style="background:linear-gradient(#6b6253,#2a2620)"></div><div class="label">CROWN</div></div>
<div class="cat" style="left:610px"><div class="img" role="img" aria-label="Fur-trimmed crown on stacked books" style="background:linear-gradient(#d8cfc2,#4a4038)"></div><div class="label">CROWN</div></div>
<div class="cat" style="left:888px"><div class="img" role="img" aria-label="Stone statue beside a wooden staircase" style="background:linear-gradient(#5a3e2a,#2e1f15)"></div><div class="label">STATUCHUE</div></div>

<section class="about" role="img" aria-label="Photograph of old leather-bound books on a shelf">
  <div class="about-card">
    <div class="inner"></div>
    <div class="about-kicker">ABOUT US</div>
    <div class="about-title"><b>HARROW</b> LANE</div>
    <p class="about-text">Lorem Ipsum is simply dummy text of the printing and typesetting industry. Lorem Ipsum has been the industry's standard dummy text ever since the 1500s, when an unknown printer.</p>
    <div class="btn" style="left:164px;top:231px;width:130px;height:31px;line-height:31px;font-size:11px">LEARN MORE</div>
  </div>
</section>

<h2 class="sec-title" style="top:1774px">SHOP <b>ONLINE</b></h2>
<div class="sec-rule" style="top:1818px"></div>

<div class="card" style="left:94px"><div class="img" role="img" aria-label="Carved gilded antique frame" style="background:linear-gradient(135deg,#8a6a3a,#3b2a18)"></div><div class="name">PRODUCT ANTIQUE CHAIR</div><div class="price">$1,350.00</div></div>
<div class="card" style="left:439px"><div class="img" role="img" aria-label="Green plant in a silver vase" style="background:linear-gradient(#c8bca8,#8a8a70)"></div><div class="name">PRODUCT ANTIQUE CHAIR</div><div class="price">$1,350.00</div></div>
<div class="card" style="left:786px"><div class="img" role="img" aria-label="Wooden frame with patterned fabric" style="background:linear-gradient(#ddd5c6,#a99a82)"></div><div class="name">PRODUCT ANTIQUE CHAIR</div><div class="price">$1,350.00</div></div>
<div class="sdot" style="left:580px;background:var(--accent)"></div>
<div class="sdot" style="left:598px"></div>
<div class="sdot" style="left:616px"></div>

<section class="popular">
  <h2 class="sec-title" style="top:58px"><b>POPULAR</b> ITEMS</h2>
  <div class="sec-rule" style="top:109px;left:601px"></div>
  <div class="pop" style="left:110px"><div class="img" role="img" aria-label="Drawer of ribbons, fabrics and accessories" style="background:linear-gradient(135deg,#b5ab96,#3a352e)"></div><div class="name">JEWELERY ITEMS</div><div class="price">$1,150.00</div></div>
  <div class="pop" style="left:628px"><div class="img" role="img" aria-label="Wood-panelled hallway with staircase and statue" style="background:linear-gradient(135deg,#6a4a30,#2a1a10)"></div><div class="name">HIGH END PURSES</div><div class="price">$750.00</div></div>
</section>

<h2 class="nl-title" style="top:2986px;font-weight:600">SIGN UP TO OUR NEWSLETTER</h2>
<h2 class="nl-title" style="top:3020px;font-weight:400">TO STAY UP TO DATE</h2>
<div class="field" style="left:176px;width:324px">Your Name</div>
<div class="field" style="left:514px;width:325px">Your Email address</div>
<div class="btn" style="left:850px;top:3098px;width:176px;height:46px;line-height:46px;font-size:14px;letter-spacing:2px;font-weight:600">SUBSCRIBE</div>

<footer class="footer">
  <div class="fcol" style="left:158px"><h4>ABOUT US</h4><ul><li>A Family Business</li><li>Philosophy and Ethos</li><li>Charity and Community</li><li>Press</li><li>Careers</li></ul></div>
  <div class="fdiv" style="left:358px"></div>
  <div class="fcol" style="left:428px"><h4>SPECIAL EVENTS</h4><ul><li>Workshops</li><li>Private Events Richmond</li><li>Private Events Covent Garden</li><li>Supper Clubs</li></ul></div>
  <div class="fdiv" style="left:656px"></div>
  <div class="fcol" style="left:736px"><h4>RESOURCES</h4><ul><li>Terms and Conditions</li><li>Privacy Policy</li><li>Contact</li></ul></div>
  <div class="fdiv" style="left:917px"></div>
  <div class="fcol" style="left:984px"><h4>SOCIAL</h4><ul><li>Photo Journal</li><li>Friends Page</li><li>Pin Board</li><li>Short Notes</li></ul></div>
  <div class="fbar"></div>
  <div class="fsmall" style="left:179px">2021 © Harrow Lane &nbsp;|&nbsp; All Right Reserved</div>
  <div class="fbrand">HARROW LANE</div>
  <div class="fsmall" style="left:887px">Cookies</div>
  <div class="fsmall" style="left:942px">Sitemap</div>
  <div class="fsmall" style="left:998px">Terms of Use</div>
</footer>

</body>
</html>
```